Big Room Track needs a CD cover!

I need a CD cover for a Big Room track which will be released soon. Please orientate at the cover of any existing track. It would be good to find a design which fits this. Its planned to generate a child of corporate design for upcoming releases. Please find a demo of the track and my logo to use in the cover. The name of the track is not found yet. Please use a short demo text to show where the title could be so I can add it afterwards.

Target Market(s)

Music streaming services. EDM Scene. Festival. Promotion.

Colors

Designer to choose colors to be used in the design.

Requirements
Must have
• Needs to be kind of a corporate design with the existing cover of another released track of mine. (Not the exact picture but use of logo and track title in this font). Needs to match the feel of the track (demo provided).
Nice to have
• Should reflect the energy of the track. Light colors are appreciated.
Should not have
• No kiddy pictures (like comic or something).

```html
<!DOCTYPE html>
<html lang="en">
<head>
<meta charset="UTF-8">
<title>Big Room – Release Cover</title>
<link href="https://fonts.googleapis.com/css2?family=Anton&display=swap" rel="stylesheet">
<style>
  :root {
    --space-deep: #07091a;
    --space-mid: #141a3a;
    --ring-blue: #6f96c2;
    --ornament-tone: #1a2233;
    --bloom-core: #1e5fd8;
    --bloom-light: #6aa6ff;
    --bloom-edge: #0b2a6e;
    --title-white: #ffffff;
  }
  html, body {
    margin: 0;
    padding: 0;
    width: 1200px;
    height: 1200px;
    overflow: hidden;
    background: var(--space-deep);
  }
  .cover {
    position: relative;
    width: 1200px;
    height: 1200px;
    overflow: hidden;
  }
  .starfield {
    position: absolute;
    inset: 0;
    background:
      radial-gradient(ellipse at 70% 10%, #1c1f52 0%, transparent 45%),
      radial-gradient(ellipse at 20% 85%, #1b1a4a 0%, transparent 50%),
      linear-gradient(160deg, var(--space-mid), var(--space-deep));
  }
  .emblem {
    position: absolute;
    inset: 0;
  }
  .track-title {
    position: absolute;
    left: 0;
    right: 0;
    top: 505px;
    margin: 0;
    text-align: center;
    font-family: "Anton", "Oswald", sans-serif;
    font-weight: 400;
    font-size: 196px;
    line-height: 1;
    letter-spacing: -6px;
    color: var(--title-white);
    transform: scaleX(0.86);
  }
  .label-name {
    position: absolute;
    left: 788px;
    top: 1090px;
    width: 380px;
    text-align: center;
    font-family: "Anton", "Oswald", sans-serif;
    font-size: 56px;
    line-height: 1;
    letter-spacing: 10px;
    color: var(--title-white);
  }
</style>
</head>
<body>
<main class="cover">
  <div class="starfield" role="img" aria-label="Starry night sky background"></div>

  <svg class="emblem" width="1200" height="1200" viewBox="0 0 1200 1200">
    <defs>
      <radialGradient id="bloomGradient" cx="50%" cy="48%" r="50%">
        <stop offset="0%" stop-color="var(--bloom-core)"/>
        <stop offset="55%" stop-color="var(--bloom-light)"/>
        <stop offset="85%" stop-color="var(--bloom-core)"/>
        <stop offset="100%" stop-color="var(--bloom-edge)"/>
      </radialGradient>
    </defs>

    <g class="frame-rings" fill="none" stroke="var(--ring-blue)" stroke-width="6">
      <circle cx="600" cy="596" r="512" stroke-dasharray="520 60 300 40 700 80 420 90 600 ..." transform="rotate(-100 600 596)"/>
      <circle cx="600" cy="596" r="488" stroke-dasharray="380 70 640 90 520 50 760 60" transform="rotate(20 600 596)"/>
      <circle cx="600" cy="596" r="440" stroke-dasharray="460 90 540 70 380 80 690 90" transform="rotate(200 600 596)"/>
    </g>

    <circle class="ornament-ring" cx="600" cy="596" r="428" fill="var(--ornament-tone)"
            role="img" aria-label="Decorative mandala ring pattern"/>
    <circle class="ornament-inner" cx="600" cy="596" r="360" fill="#05070f"/>

    <circle class="bloom" cx="600" cy="596" r="350" fill="url(#bloomGradient)"
            role="img" aria-label="Glowing blue dandelion seed head photograph"/>
  </svg>

  <h1 class="track-title">BIG ROOM</h1>
  <div class="label-name">ENVOYA</div>
</main>
</body>
</html>
```